RZO Design tag

Looking to design a tag for our new hat & glove brand RZO Design. These are winter hats & gloves. Long story short these are lower cost/retail items but I'm trying to convey higher quality goods through a nice tag. I’ve attached a tag of another brand we have to give you a general idea of what I’d be looking for- but again for our new brand RZO Design.
I’m thinking we can do one general design- and then do it in 4 different color schemes: First one mimicking the attachment’s colors for ladies items- so a few different shades of pink. Then 2nd color scheme a darker more masculine color tone for mens or unisex items- maybe blue/dark blue, and then a 3rd color scheme for kids items that is more vibrant/kid like colors. Last one red & green for some Christmas items we do.
A few things:
• Trying to make the tags look classy as possible
• The tag will need to measure 2.25” high x 2” wide. The top little bit would have to be space left blank for a hole punch- just like on the attached sample tag. But again the tags designed would need to be 2.25" tall x 2" wide so not the same shape as the sample tag.
• For item name you can just put “Knit Hat” for the generic tag item name (in place of what says on the same “Chenille Slipper Bootie”). Please try to keep the writing a nice font similar to what is on this tag- again trying to have a classy tag look
• On the bottom center (In place of Made in China) it would just need to say “One Size” in standard font
Hope this helps & thank you
Target Market(s)
People buying winter hats & gloves
Industry/Entity Type
Retail- winter hats & gloves
Look and feel

```html
<!DOCTYPE html>
<html lang="en">
<head>
<meta charset="utf-8">
<title>RZO Design – Knit Hat Tags</title>
<link rel="stylesheet" href="https://fonts.googleapis.com/css2?family=Kaushan+Script&family=Montserrat:wght@600&display=swap">
<style>
  :root {
    --stage-dark: #050505;
    --stage-mid: #5a5a5a;
    --stage-light: #f3f3f3;
    --pink: #ef6faf;
    --blue: #233a9b;
    --yellow: #fff200;
    --red: #ec1c24;
    --green: #066b38;
    --ink: #000000;
    --paper: #ffffff;
    --silver-hi: #ffffff;
    --silver-lo: #a9a9ab;
    --graphite-hi: #9a9a9c;
    --graphite-lo: #2d2d2f;
  }
  * { box-sizing: border-box; margin: 0; padding: 0; }
  html, body { width: 1200px; height: 990px; overflow: hidden; }
  body {
    position: relative;
    background: linear-gradient(35deg, var(--stage-dark) 0%, #2a2a2a 25%, var(--stage-mid) 50%, #a5a5a5 75%, var(--stage-light) 100%);
    font-family: "Montserrat", sans-serif;
  }

  .tag {
    position: absolute;
    width: 276px;
    height: 310px;
    background: var(--tag-bg);
    box-shadow: 0 10px 28px rgba(0,0,0,0.55);
    overflow: hidden;
  }
  .tag--ladies        { left: 111px; top: 134px; --tag-bg: var(--pink);   --label: var(--paper); }
  .tag--mens          { left: 462px; top: 134px; --tag-bg: var(--blue);   --label: var(--paper); }
  .tag--kids          { left: 812px; top: 134px; --tag-bg: var(--yellow); --label: var(--ink); }
  .tag--holiday-red   { left: 286px; top: 546px; --tag-bg: var(--red);    --label: var(--paper); }
  .tag--holiday-green { left: 637px; top: 546px; --tag-bg: var(--green);  --label: var(--paper); }

  .tag__pattern {
    position: absolute;
    inset: 0;
    background: linear-gradient(160deg, rgba(0,0,0,0.05) 0%, rgba(0,0,0,0) 45%, rgba(0,0,0,0.06) 100%);
  }
  .tag__frame {
    position: absolute;
    inset: 12px 11px 11px 11px;
    border: 1px solid var(--label);
  }
  .tag__brand {
    position: absolute;
    left: 0;
    right: 0;
    top: 80px;
    text-align: center;
    font-weight: 600;
    font-size: 16px;
    letter-spacing: 1px;
    line-height: 1;
    color: var(--label);
  }

  .tag__item {
    position: absolute;
    font-family: "Kaushan Script", cursive;
    font-size: 66px;
    line-height: 1;
    white-space: nowrap;
  }
  .tag__item--first  { left: 54px;  top: 126px; }
  .tag__item--second { left: 110px; top: 186px; }

  .tag__item--silver {
    background: linear-gradient(170deg, var(--silver-hi) 10%, var(--silver-lo) 50%, var(--silver-hi) 85%);
    -webkit-background-clip: text;
    background-clip: text;
    color: transparent;
    filter: drop-shadow(2px 2px 1px rgba(0,0,0,0.18));
  }
  .tag__item--graphite {
    background: linear-gradient(170deg, var(--graphite-lo) 10%, var(--graphite-hi) 50%, var(--graphite-lo) 85%);
    -webkit-background-clip: text;
    background-clip: text;
    color: transparent;
    filter: drop-shadow(2px 2px 1px rgba(0,0,0,0.2));
  }
  .tag__item--green { color: var(--green); text-shadow: -2px 2px 0 var(--paper); }
  .tag__item--red   { color: var(--red);   text-shadow: -2px 2px 0 var(--paper); }

  .tag__size {
    position: absolute;
    left: 0;
    right: 0;
    top: 276px;
    text-align: center;
    font-weight: 600;
    font-size: 10px;
    letter-spacing: 2.6px;
    color: var(--label);
  }
</style>
</head>
<body>

  <section class="tag tag--ladies">
    <div class="tag__pattern" role="img" aria-label="Faint repeated brand name pattern"></div>
    <div class="tag__frame"></div>
    <div class="tag__brand">RZO Design</div>
    <div class="tag__item tag__item--first tag__item--silver">Knit</div>
    <div class="tag__item tag__item--second tag__item--silver">Hat</div>
    <div class="tag__size">ONE SIZE</div>
  </section>

  <section class="tag tag--mens">
    <div class="tag__pattern" role="img" aria-label="Faint repeated brand name pattern"></div>
    <div class="tag__frame"></div>
    <div class="tag__brand">RZO Design</div>
    <div class="tag__item tag__item--first tag__item--silver">Knit</div>
    <div class="tag__item tag__item--second tag__item--silver">Hat</div>
    <div class="tag__size">ONE SIZE</div>
  </section>

  <section class="tag tag--kids">
    <div class="tag__pattern" role="img" aria-label="Faint repeated brand name pattern"></div>
    <div class="tag__frame"></div>
    <div class="tag__brand">RZO Design</div>
    <div class="tag__item tag__item--first tag__item--graphite">Knit</div>
    <div class="tag__item tag__item--second tag__item--graphite">Hat</div>
    <div class="tag__size">ONE SIZE</div>
  </section>

  <section class="tag tag--holiday-red">
    <div class="tag__pattern" role="img" aria-label="Faint repeated brand name pattern"></div>
    <div class="tag__frame"></div>
    <div class="tag__brand">RZO Design</div>
    <div class="tag__item tag__item--first tag__item--green">Knit</div>
    <div class="tag__item tag__item--second tag__item--green">Hat</div>
    <div class="tag__size">ONE SIZE</div>
  </section>

  <section class="tag tag--holiday-green">
    <div class="tag__pattern" role="img" aria-label="Faint repeated brand name pattern"></div>
    <div class="tag__frame"></div>
    <div class="tag__brand">RZO Design</div>
    <div class="tag__item tag__item--first tag__item--red">Knit</div>
    <div class="tag__item tag__item--second tag__item--red">Hat</div>
    <div class="tag__size">ONE SIZE</div>
  </section>

</body>
</html>
```